Business Card Design

We need a business card design for a Non-Profit Christian Based Organization located in Milford, Pa.
Alder Ridge Helping Harbor
Is a Christ-centered organization dedicated to providing compassion and hope to homeless or near homeless, families and individuals, by meeting their basic and urgent need of food, clothing and shelter.
Updates
the logo is black and white
and must add the color green some where 00400
Industry/Entity Type
Clothing
Contact Information for Business Card
Alder Ridge Helping Harbor
P.O. Box 287
Milord, Pa 18337
Phone: (570) 413-CARE(2273)
Toll Free: (855) 413-CARE
email:Info@alderridgehh.org
email:Careline@alderridgehh.org
Our organization already has a logo.
Front of card:
Is a Christ-centered organization dedicated to providing compassion and hope to homeless or near homes, families and individual by meeting their basic and urgent need of food, clothing and shelter.(this is our Mission Statement)
On back of card:
'I was hungry and you gave me something to eat;
"I was thirsty and you gave me something to drink;
"I was a stranger and you invited me in."
Matthew 25:35
Color: Logo is black and white
Background color I would like a bright light green 00ff00(close to that)
I attached a sample of what I created on Quill Press but, I don't like the color green, nor the design (but I just wanted to give you and Idea of the Logo and Alder Ridge (one line) Helping Harbor (second line) in a different font thank you
Delia Rostova
Pr/Board of Directors

```html
<!DOCTYPE html>
<html lang="en">
<head>
<meta charset="utf-8">
<title>Alder Ridge Helping Harbor – Card Back</title>
<link rel="stylesheet" href="https://fonts.googleapis.com/css2?family=Arimo:wght@500;700&display=swap">
<style>
  :root {
    --card-green: #68bc45;
    --card-white: #ffffff;
  }
  html, body {
    margin: 0;
    padding: 0;
    width: 1200px;
    height: 686px;
    overflow: hidden;
    background: var(--card-green);
  }
  .card-back {
    position: relative;
    width: 1200px;
    height: 686px;
    background: var(--card-green);
    color: var(--card-white);
    font-family: "Arimo", "Helvetica Neue", Arial, sans-serif;
  }
  .scripture-quote {
    position: absolute;
    left: 50px;
    top: 52px;
    margin: 0;
    font-weight: 700;
    font-size: 89px;
    line-height: 111px;
    letter-spacing: -0.2px;
  }
  .scripture-quote .quote-line {
    display: block;
    white-space: nowrap;
  }
  .scripture-reference {
    position: absolute;
    right: 62px;
    top: 566px;
    margin: 0;
    font-weight: 500;
    font-size: 52px;
    line-height: 1;
  }
</style>
</head>
<body>
  <main class="card-back">
    <blockquote class="scripture-quote">
      <span class="quote-line">"I was thirsty and you</span>
      <span class="quote-line">gave me something to</span>
      <span class="quote-line">drink; I was a stranger</span>
      <span class="quote-line">and you invited me in."</span>
    </blockquote>
    <p class="scripture-reference">Matthew 25:35</p>
  </main>
</body>
</html>
```